GUARANTEED WordPress design needed for a sassy, confident charisma coach!

We need a website design for Mira Haskett's brand new, responsive, Wordpress website.
Mira is a trainer / coach who teaches people how to be more charismatic and runs events, publishes video courses and has an ongoing video blog. Her old website is here: www.mirahaskett-example.co.uk ... but it's now time to have a much better site!
We have a strong idea about the technical components of the website, but we need a designer's eye to create a great style for the site (and provide layered PSD files which our developers will then convert to HTML and CSS).
Mira's brand is sassy, brave, warm and confident. The videos on her existing site give quite a good feel for her personality. We need a clean, stylish and compelling page that isn't too corporate and captures her personality. Every element needs to feel coherent, from fonts and headings to colours and spacing.
The following sites are not exactly what Mira wants (and certainly aren't right in terms of colours) but they give you an idea of the kind of people she is competing against and the area she is operating in:
http://www.fenna-troske.example/
http://brynwellow.example/
Ideally, you will have done something similar and be able to key in on exactly the kind of thing we want: we're not looking to reinvent the wheel. Hopefully you won't mind tweaking a few things if you are close to what we need.
More detail is provided in the word document attached. But in a nutshell we need: a banner, footer, sign-up strap, menu bar, signature and 4 different basic page types. We want bursts of bright colours, contrasted with black and white if possible - sorry we can't be more specific than that...
The word doc also contains some amateur mock-ups as well (the images are also just mockups at this stage) - but although these give a general sense of the structure what we are looking for, we are clearly not designers...so please help! We need a designer's touch!
Kind regards,
Tomas
PS The layered PSD versions of the mockup files are available on Quellbox: https://files.quellbox.example/sh/k27rpw4m1xqzv/QWxnEr8tLpVu3YcMd0aHs?dl=0
Project Deadline Extended Reason: We are looking for a polished, "designed" look. The mock-up that we have provided is just indicative of the features we want. Added Saturday, May 14, 2016
Entrepreneurs who need to sell themselves.
4 page

```html
<!DOCTYPE html>
<html lang="en">
<head>
<meta charset="utf-8">
<title>Mira Haskett – Charisma Coach</title>
<link rel="stylesheet" href="https://fonts.googleapis.com/css2?family=Open+Sans:wght@400;600&family=Roboto:wght@400;500;700&display=swap">
<style>
:root{
  --pink:#cc0a7e;
  --pink-soft:#e9a3c7;
  --green:#8dc21f;
  --green-soft:#cfe3a8;
  --ink:#333;
  --muted:#888;
  --line:#e2e2e2;
  --page:#f5f5f5;
  --white:#fff;
}
*{box-sizing:border-box;margin:0;padding:0}
html,body{width:1200px;height:2305px;overflow:hidden}
body{position:relative;background:var(--white);font-family:"Open Sans",Arial,sans-serif;color:var(--ink)}
.abs{position:absolute}

/* header */
.site-header{left:0;top:0;width:1200px;height:51px;background:var(--white);box-shadow:0 1px 3px rgba(0,0,0,.08);z-index:5}
.brand{left:89px;top:10px;font-size:24px;font-weight:600;color:var(--pink)}
.nav a{position:absolute;top:17px;font-size:13px;color:#444;text-decoration:none}
.nav a.current{color:var(--pink)}
.nav .underline{position:absolute;left:674px;top:47px;width:52px;height:3px;background:var(--pink)}

/* hero */
.hero{left:0;top:51px;width:1200px;height:453px;overflow:hidden}
.hero-word{font-family:"Roboto",Arial,sans-serif;font-weight:700;color:var(--pink-soft);font-size:152px;left:266px;top:128px;letter-spacing:2px;line-height:1}
.hero-sub{font-family:"Roboto",Arial,sans-serif;font-weight:400;color:var(--green-soft);font-size:80px;left:262px;top:282px;line-height:1}
.hero-frame{left:492px;top:108px;width:215px;height:284px;border:2px solid var(--pink)}
.hero-portrait{left:410px;top:24px;width:260px;height:430px;background:linear-gradient(180deg,#3a2b2a 0%,#e8262f 25%,#e32a2f 75%,#222 100%);border-radius:90px 90px 10px 10px}

/* sign-up strap */
.strap{left:0;top:504px;width:1200px;height:142px;background:var(--pink)}
.monitor{left:207px;top:473px;width:196px;height:157px}
.strap-copy{left:453px;top:521px;width:460px;font-size:12.5px;line-height:20px;color:var(--white)}
.field{background:var(--white);height:40px;font-size:13px;color:#555;padding:11px 14px}
.strap .field{position:absolute;top:60px}
.btn-yes{border-radius:50%;background:var(--green);color:var(--white);font-size:11px;font-weight:600;display:flex;align-items:center;justify-content:center;text-align:center;line-height:14px;border:3px solid #fff}
.strap-note{left:453px;top:606px;font-size:11.5px;color:var(--white)}

/* main */
.main{left:0;top:646px;width:1200px;height:1360px;background:var(--page)}
.card{background:var(--white);border:1px solid var(--line)}
.video-media{left:0;top:0;width:633px;height:357px;background:linear-gradient(135deg,#6a6a6a,#d8d0cc 45%,#b43a3a 75%,#ededed)}
.play{left:529px;top:286px;width:64px;height:40px;background:var(--green)}
.video-copy{left:30px;top:384px;width:570px;font-size:14px;line-height:28px;color:#555}
.video-meta{left:0;top:459px;width:633px;border-top:1px solid var(--line);height:62px;display:flex;justify-content:center;align-items:center;gap:22px;font-size:11.5px;color:#999;text-transform:uppercase}
.video-meta span{display:flex;align-items:center;gap:6px}

.audience-media{left:0;top:0;width:284px;height:230px}
.audience-title{left:318px;top:52px;font-family:"Roboto",Arial,sans-serif;font-size:18px;color:#333}
.audience-copy{left:318px;top:84px;width:290px;font-size:13px;line-height:20px;color:#555}
.audience-link{left:318px;top:150px;font-size:13px;line-height:18px;color:var(--pink)}

.section-title{font-family:"Roboto",Arial,sans-serif;font-size:22px;color:#333}
.quote{background:var(--white);font-size:12px;line-height:20px;color:#555;padding:16px 22px}
.quote-tail{width:0;height:0;border-top:22px solid var(--pink);border-right:22px solid transparent}
.avatar{width:60px;height:60px;border-radius:50%;border:3px solid var(--green-soft);background:linear-gradient(#c9b9a6,#8a7564)}
.person{font-size:11.5px;line-height:20px;color:#555}
.person small{display:block;font-size:11px;color:#999}

/* sidebar */
.sidebar{left:775px;top:0;width:336px;height:1199px;background:var(--white)}
.widget{background:var(--white);border:1px solid var(--line)}
.widget-title{font-family:"Roboto",Arial,sans-serif;font-size:18px;color:#222}
.widget-title em{font-style:normal;color:var(--pink)}
.widget-rule{height:1px;background:var(--line)}
.tweet{font-size:11px;line-height:16px;color:#444}
.tweet b{font-weight:600;color:#222}
.tweet .handle{color:#999}
.tweet a{color:#3a8fd0;text-decoration:none}
.tweet-pic{width:28px;height:28px;background:linear-gradient(#6b5a52,#b9a79a)}
.tip-thumb{width:123px;height:71px}
.tip-text{font-size:12px;line-height:18px;color:#444;width:135px}
.tip-text a{color:var(--pink);text-decoration:none;display:block}
.partner{height:38px;border-radius:4px;background:#ececec}

/* newsletter */
.newsletter-title{left:0;top:2043px;width:1200px;text-align:center;font-size:22px;color:var(--pink);letter-spacing:.5px}
.newsletter-copy{left:360px;top:2080px;width:480px;text-align:center;font-size:11.5px;line-height:20px;color:#555}
.newsletter .field{position:absolute;top:2137px;height:36px;border:1px solid #d8d8d8;padding:9px 16px}
.sad{left:0;top:2183px;width:1200px;text-align:center;font-size:11.5px;color:#555}
.social{top:2207px;width:31px;height:31px;border-radius:50%;background:#2a5d9c;color:#fff;font-size:9px;font-weight:600;display:flex;align-items:center;justify-content:center}

.site-footer{left:0;top:2265px;width:1200px;height:40px;background:var(--pink);font-size:11.5px;color:var(--white)}
.site-footer span{position:absolute;top:12px}
</style>
</head>
<body>

<header class="site-header abs">
  <div class="brand abs">Mira Haskett</div>
  <nav class="nav">
    <a class="current" style="left:684px">Home</a>
    <a style="left:745px">Events</a>
    <a style="left:811px">Work With Me</a>
    <a style="left:917px">Corporate</a>
    <a style="left:1002px">About</a>
    <a style="left:1066px">Contact</a>
    <span class="underline"></span>
  </nav>
</header>

<section class="hero abs">
  <div class="hero-word abs">ATTRACT</div>
  <div class="hero-sub abs">Connect Influence</div>
  <div class="hero-frame abs"></div>
  <div class="hero-portrait abs" role="img" aria-label="Full-length photo of the coach in a red jumpsuit, hand on hip"></div>
</section>

<section class="strap abs">
  <p class="strap-copy abs" style="top:17px">Learn how to unlock the superpower* of your charisma and win all the business you want with this free training.*</p>
  <div class="field" style="left:453px;width:216px">Name*</div>
  <div class="field" style="left:676px;width:216px">Email*</div>
  <div class="btn-yes abs" style="left:900px;top:54px;width:58px;height:58px">Yes<br>Please</div>
  <p class="strap-note abs" style="top:102px">* Promise to only use your powers for good</p>
</section>

<div class="monitor abs" role="img" aria-label="Desktop monitor showing a still from the free training video">
  <svg width="196" height="157" viewBox="0 0 196 157">
    <rect x="0" y="0" width="196" height="124" rx="6" fill="#1e1e1e"/>
    <rect x="8" y="8" width="180" height="104" fill="#c9c1bd"/>
    <rect x="0" y="112" width="196" height="14" fill="#dcdcdc"/>
    <polygon points="82,126 114,126 120,148 76,148" fill="#cfcfcf"/>
    <rect x="62" y="148" width="72" height="5" rx="2" fill="#bdbdbd"/>
  </svg>
</div>

<main class="main abs">
  <article class="card abs" style="left:120px;top:35px;width:633px;height:521px">
    <div class="video-media abs" role="img" aria-label="Video still of the coach talking to camera in a colourful studio"></div>
    <div class="play abs">
      <svg width="64" height="40" viewBox="0 0 64 40"><polygon points="26,11 26,29 41,20" fill="#fff"/></svg>
    </div>
    <p class="video-copy abs">Duis dapibus fermentum orci, nec malesuada libero vehicula ut. Integer sodales, urna eget interdum eleifend, nulla nibh laoreet nisl, quis dignissim mauris dolor eget mi.</p>
    <div class="video-meta abs">
      <span><svg width="12" height="12" viewBox="0 0 12 12"><path d="M5 1H1v10h10V7M7 1h4v4M11 1 5 7" fill="none" stroke="#999" stroke-width="1.4"/></svg>Permalink</span>
      <span><svg width="12" height="12" viewBox="0 0 12 12"><circle cx="6" cy="6" r="5" fill="none" stroke="#999" stroke-width="1.4"/><path d="M6 3v3h2" fill="none" stroke="#999" stroke-width="1.4"/></svg>Feb 8, 2015</span>
      <span><svg width="12" height="12" viewBox="0 0 12 12"><path d="M6 11 1 6a2.8 2.8 0 0 1 5-3.5A2.8 2.8 0 0 1 11 6z" fill="#999"/></svg>Likes</span>
      <span><svg width="12" height="12" viewBox="0 0 12 12"><path d="M2 5V3h8L8 1M10 7v2H2l2 2" fill="none" stroke="#999" stroke-width="1.4"/></svg>Reblog</span>
      <span><svg width="12" height="12" viewBox="0 0 12 12"><circle cx="9" cy="2.5" r="1.8" fill="#999"/><circle cx="3" cy="6" r="1.8" fill="#999"/><circle cx="9" cy="9.5" r="1.8" fill="#999"/><path d="M9 2.5 3 6l6 3.5" stroke="#999" fill="none"/></svg>Share</span>
    </div>
  </article>

  <article class="card abs" style="left:120px;top:581px;width:633px;height:230px">
    <div class="audience-media abs" style="background:linear-gradient(135deg,#e9e9ec,#6d6d78 50%,#e0d06a)" role="img" aria-label="Photo of the coach advising an individual client"></div>
    <h3 class="audience-title abs">Individual</h3>
    <p class="audience-copy abs">You are a professional who is frustrated with your image. You want looking good to be easy, but don't know where to start.</p>
    <a class="audience-link abs">Click here to<br>make image easy</a>
  </article>

  <article class="card abs" style="left:120px;top:830px;width:633px;height:230px">
    <div class="audience-media abs" style="background:linear-gradient(135deg,#e6e2e2,#b53a45 55%,#3a3a40)" role="img" aria-label="Photo of a business audience seated at a workshop"></div>
    <h3 class="audience-title abs">Business</h3>
    <p class="audience-copy abs">You are a medium to large sized business who wants your employees to project a more confident, professional image.</p>
    <a class="audience-link abs">Click here to<br>make image easy</a>
  </article>

  <h2 class="section-title abs" style="left:123px;top:1089px">Success Stories</h2>

  <blockquote class="quote abs" style="left:120px;top:1129px;width:310px;height:97px">"I've never been a fashionista and my wardrobe was dominated by the colour black... my appearance in terms of make-up .</blockquote>
  <div class="quote-tail abs" style="left:120px;top:1226px"></div>
  <div class="avatar abs" style="left:133px;top:1258px" role="img" aria-label="Client portrait"></div>
  <p class="person abs" style="left:207px;top:1270px">Maria - HR Director<small>From: Sassari (SS)</small></p>

  <blockquote class="quote abs" style="left:443px;top:1129px;width:310px;height:97px">"I visited Mira for a 1 to 1 impact session. I've recently set up my own business and wanted to ensure that.</blockquote>
  <div class="quote-tail abs" style="left:443px;top:1226px"></div>
  <div class="avatar abs" style="left:456px;top:1258px;background:linear-gradient(#e4cf9a,#a88d60)" role="img" aria-label="Client portrait"></div>
  <p class="person abs" style="left:530px;top:1270px">Maria - HR Director<small>From: Sassari (SS)</small></p>

  <aside class="sidebar abs">
    <section class="widget abs" style="left:23px;top:35px;width:290px;height:292px">
      <h3 class="widget-title abs" style="left:18px;top:10px">Tweets <em style="font-size:12px">by @mirahaskettltd</em></h3>
      <div class="abs" style="left:276px;top:12px;width:4px;height:26px;background:var(--pink);border-radius:2px"></div>
      <div class="widget-rule abs" style="left:12px;top:40px;width:260px"></div>
      <div class="tweet-pic abs" style="left:20px;top:52px" role="img" aria-label="Profile photo"></div>
      <p class="tweet abs" style="left:56px;top:50px;width:210px"><b>Mira Haskett</b><br><span class="handle">@mirahaskettltd</span></p>
      <p class="tweet abs" style="left:20px;top:90px;width:250px"><a>#mondaymotivation</a> it's all about which way you look x <a>fb.example/PVcZOZgO</a></p>
      <div class="widget-rule abs" style="left:12px;top:158px;width:260px"></div>
      <div class="tweet-pic abs" style="left:20px;top:170px" role="img" aria-label="Profile photo"></div>
      <p class="tweet abs" style="left:56px;top:168px;width:210px"><b>Mira Haskett</b><br><span class="handle">@mirahaskettltd</span></p>
      <p class="tweet abs" style="left:20px;top:208px;width:250px">Going to miss waking up to this every day, but looking forward to getting back to London too.</p>
    </section>

    <section class="widget abs" style="left:23px;top:339px;width:290px;height:410px">
      <h3 class="widget-title abs" style="left:18px;top:14px">Latest Tips <em>&amp; Videos</em></h3>
      <div class="widget-rule abs" style="left:14px;top:44px;width:262px"></div>
      <div class="tip-thumb abs" style="left:14px;top:65px;background:linear-gradient(135deg,#777,#c9c1bd 50%,#b53a3a)" role="img" aria-label="Video thumbnail"></div>
      <p class="tip-text abs" style="left:146px;top:63px">Networking made easy - top tips to network like a pro<a>Read More</a></p>
      <div class="tip-thumb abs" style="left:14px;top:146px;background:linear-gradient(135deg,#1d1d1d,#7a5a3a 55%,#2a2a2a)" role="img" aria-label="Video thumbnail"></div>
      <p class="tip-text abs" style="left:146px;top:144px">Brightmark Survival Guide - for Grown-Ups!<a>Read More</a></p>
      <div class="tip-thumb abs" style="left:14px;top:228px;background:linear-gradient(135deg,#f4f4f4,#2e7d4f 40%,#d6335a 70%,#f0f0f0)" role="img" aria-label="Capsule wardrobe flat lay"></div>
      <p class="tip-text abs" style="left:146px;top:226px">How to build a capsule wardrobe<a>Read More</a></p>
      <div class="tip-thumb abs" style="left:14px;top:315px;background:linear-gradient(135deg,#f2f2f2,#333 45%,#c9b6a0 80%)" role="img" aria-label="Wardrobe clothing flat lay"></div>
      <p class="tip-text abs" style="left:146px;top:313px">Wardrobe detox - out with the old.<a>Read More</a></p>
    </section>

    <section class="widget abs" style="left:23px;top:762px;width:290px;height:406px">
      <h3 class="widget-title abs" style="left:18px;top:14px">Partners</h3>
      <div class="widget-rule abs" style="left:14px;top:44px;width:262px"></div>
      <div class="partner abs" style="left:17px;top:77px;width:125px"></div>
      <div class="partner abs" style="left:158px;top:77px;width:115px"></div>
      <div class="partner abs" style="left:17px;top:134px;width:125px"></div>
      <div class="partner abs" style="left:158px;top:134px;width:115px"></div>
      <div class="partner abs" style="left:17px;top:193px;width:125px;height:52px"></div>
      <div class="partner abs" style="left:158px;top:197px;width:115px;height:42px"></div>
      <div class="partner abs" style="left:17px;top:270px;width:125px;height:56px"></div>
      <div class="partner abs" style="left:158px;top:277px;width:115px"></div>
      <div class="partner abs" style="left:17px;top:342px;width:125px"></div>
      <div class="partner abs" style="left:158px;top:342px;width:115px"></div>
    </section>
  </aside>
</main>

<section class="newsletter">
  <h2 class="newsletter-title abs">SUBSRIBE NEWSLETTER</h2>
  <p class="newsletter-copy abs">Hey! Don't go without signing up because you'll miss out on exclusive offers, awesome tips, and weekly motivation in my fab newsletter*.</p>
  <div class="field" style="left:363px;width:236px">First Name</div>
  <div class="field" style="left:610px;width:237px">Email</div>
  <div class="btn-yes abs" style="left:859px;top:2127px;width:58px;height:58px">Yes<br>Please</div>
  <p class="sad abs">And that'll make me a sad :-(</p>
  <div class="social abs" style="left:545px">Hub</div>
  <div class="social abs" style="left:584px;background:#2a9bd8">Chat</div>
  <div class="social abs" style="left:623px;background:#1d5a8a">Net</div>
</section>

<footer class="site-footer abs">
  <span style="left:375px">Copyright © 2016 . Mira Haskett</span>
  <span style="left:593px">Privacy Policy</span>
  <span style="left:681px">Terms Policy</span>
  <span style="left:762px">Disclaimer</span>
</footer>

</body>
</html>
```